Toravelle Works Luxury Candles

Luxury box design,, simple and sophisticated look,,

My collection of candles come in 5 different fragrances, i would like to be able to change the fragrance name on the boxes,,,,

I would like the outline of australia on the front down the bottom , (only small) to represent this is an australian product.

My boxes are white gloss,,,

Happy for you to use my current logo ,,, however you'll have to change Toravelle Nails to Toravelle Works.

```html
<!DOCTYPE html>
<html lang="en">
<head>
<meta charset="utf-8">
<title>Toravelle Works Luxury Candles – Box Panels</title>
<link rel="stylesheet" href="https://fonts.googleapis.com/css2?family=Cormorant+Garamond:wght@400;500&family=EB+Garamond:ital@1&display=swap">
<style>
  :root {
    --page: #ffffff;
    --ink: #1a1408;
    --black: #050505;
    --gold-deep: #9a7431;
    --gold-mid: #c9a54e;
    --gold-light: #f4eba2;
    --cream: #fbf8ee;
    --gold-band: linear-gradient(90deg, #a47d34 0%, #c9a650 22%, #efe39a 45%, #d2b25c 65%, #9d7532 100%);
    --gold-panel: linear-gradient(90deg, #a27a33 0%, #d4b35c 30%, #f2e8a0 52%, #cfad57 75%, #9a7330 100%);
  }
  * { margin: 0; padding: 0; box-sizing: border-box; }
  html, body { width: 1200px; height: 819px; overflow: hidden; background: var(--page); }
  .canvas { position: relative; width: 1200px; height: 819px; background: var(--page); }

  .box-face { position: absolute; top: 70px; width: 452px; height: 668px; overflow: hidden; }
  .box-face--front { left: 94px; }
  .box-face--back { left: 656px; }

  .marble {
    position: absolute; inset: 0;
    background:
      radial-gradient(ellipse at 20% 15%, var(--black) 0 18%, transparent 40%),
      radial-gradient(ellipse at 80% 30%, var(--gold-mid) 0 15%, transparent 40%),
      radial-gradient(ellipse at 30% 75%, var(--cream) 0 14%, transparent 38%),
      radial-gradient(ellipse at 75% 85%, var(--black) 0 16%, transparent 40%),
      radial-gradient(ellipse at 55% 55%, var(--gold-light) 0 10%, transparent 35%),
      linear-gradient(135deg, var(--gold-mid), var(--black) 35%, var(--cream) 60%, var(--gold-deep));
  }

  .label-band {
    position: absolute; left: 0; top: 216px; width: 100%; height: 154px;
    background: var(--gold-band);
    border-top: 3px solid var(--gold-light);
    border-bottom: 3px solid var(--gold-light);
    text-align: center; color: var(--ink);
  }
  .brand-name {
    font-family: "Cormorant Garamond", serif; font-weight: 500;
    color: var(--ink);
  }
  .label-band .brand-name { font-size: 48px; margin-top: 26px; line-height: 1.1; }
  .label-band .product-line {
    font-family: "Cormorant Garamond", serif; font-size: 17px; letter-spacing: 0.32em;
    margin-top: 10px; padding-left: 0.32em;
  }
  .fragrance-rule {
    display: flex; align-items: center; justify-content: center; gap: 8px;
    margin-top: 4px;
    font-family: "Cormorant Garamond", serif; font-size: 8px; letter-spacing: 0.25em;
  }
  .fragrance-rule::before, .fragrance-rule::after {
    content: ""; width: 62px; height: 1px; background: var(--ink);
  }

  .origin-mark {
    position: absolute; left: 20px; bottom: 24px; width: 28px; height: 28px;
    border-radius: 50%; background: var(--cream); border: 1px solid var(--gold-mid);
  }

  .info-panel {
    position: absolute; left: 102px; top: 104px; width: 248px; height: 458px;
    background: var(--gold-panel);
    border-bottom: 3px solid var(--gold-light);
    text-align: center; color: var(--ink);
  }
  .info-panel .brand-name { font-size: 28px; margin-top: 42px; line-height: 1.1; }
  .info-panel .product-line {
    font-family: "Cormorant Garamond", serif; font-size: 9px; letter-spacing: 0.3em; margin-top: 4px;
  }
  .info-panel .fragrance-name {
    font-family: "Cormorant Garamond", serif; font-size: 12px; letter-spacing: 0.3em;
    margin-top: 24px;
  }
  .description {
    font-family: "EB Garamond", serif; font-style: italic; font-size: 10.5px;
    line-height: 21px; margin-top: 10px; padding: 0 6px;
  }
</style>
</head>
<body>
<main class="canvas">
  <section class="box-face box-face--front">
    <div class="marble" role="img" aria-label="Black, gold and white marbled pattern"></div>
    <div class="label-band">
      <h1 class="brand-name">Toravelle Works</h1>
      <p class="product-line">LUXURY CANDLES</p>
      <p class="fragrance-rule">COTTON CANDY</p>
    </div>
    <div class="origin-mark" role="img" aria-label="Small outline of Australia in a circle"></div>
  </section>

  <section class="box-face box-face--back">
    <div class="marble" role="img" aria-label="Black, gold and white marbled pattern"></div>
    <div class="info-panel">
      <h2 class="brand-name">Toravelle Works</h2>
      <p class="product-line">LUXURY CANDLES</p>
      <p class="fragrance-name">COTTON CANDY</p>
      <p class="description">
        orem ipsum dolor sit amet, consectetur<br>
        adipiscing elit. Vestibulum efficitur lobortis orci<br>
        ac consequat. Ut porta pellentesque metus, sit<br>
        amet tristique turpis ornare in. Ut dignissim<br>
        ligula nisi, vitae mollis lacus mollis semper.<br>
        Nulla tincidunt porttitor nisi eget luctus.<br>
        Vestibulum efficitur fringilla enim id vehicula.<br>
        Proin suscipit, diam nec bibendum<br>
        ullamcorper, odio quam gravida libero, vel<br>
        tristique nisi turpis id purus. Phasellus ac<br>
        tincidunt magna. Sed scelerisque interdum<br>
        magna ut tempor.
      </p>
    </div>
  </section>
</main>
</body>
</html>
```